Help us share the power of history

We need 5 flyers (they can be similar in design, just small content changes in the front) and 1 large poster.

Paper Lantern? is a movement that aims to change the history market so that everyone gets what they need to be a changemaker of society. We've been selected as one of the most promising startups in Massachusetts and we will have a booth at Brightforge's Pitch Day.

We are trying to attract the attention of people walking buy to invest in our kickstarter campaign.

Target Market(s)

500-1,000 social entrepreneurs who are going to be walking around a large convention hall - so everything in terms of colors and design needs to be attractive

Industry/Entity Type

Non Profit

Font styles to use
Other font styles liked:
• Phoenix American

Colors

Designer to choose colors to be used in the design.

Requirements
Must have
• Font type: Phoenix American
• Modern
• Easy to read
• Eye-catching
• Please see attached document for more information.

```html
<!DOCTYPE html>
<html lang="en">
<head>
<meta charset="utf-8">
<title>Paper Lantern? flyer set</title>
<link href="https://fonts.googleapis.com/css2?family=Pathway+Gothic+One&family=Jost:wght@400&display=swap" rel="stylesheet">
<style>
  :root {
    --orange: #f26b22;
    --green: #2aa54a;
    --red: #f20511;
    --purple: #55307f;
    --yellow: #ffcb05;
    --ink: #1b1b1b;
    --paper: #ffffff;
    --ribbon: #5a5a5a;
    --band-light: #e4e4e4;
    --band-dark: #9a9a9a;
  }
  * { box-sizing: border-box; margin: 0; padding: 0; }
  html, body { width: 1200px; height: 1200px; overflow: hidden; background: var(--paper); }
  .sheet { position: relative; width: 1200px; height: 1200px; }

  .card {
    position: absolute; width: 250px; height: 250px; overflow: hidden;
    background: var(--accent);
    font-family: "Pathway Gothic One", "Arial Narrow", sans-serif;
  }
  .card svg.art { position: absolute; inset: 0; width: 250px; height: 250px; }

  .theme-orange { --accent: var(--orange); --back-ink: var(--ink); }
  .theme-green  { --accent: var(--green);  --back-ink: var(--ink); }
  .theme-red    { --accent: var(--red);    --back-ink: var(--ink); }
  .theme-purple { --accent: var(--purple); --back-ink: #ffffff; }
  .theme-yellow { --accent: var(--yellow); --back-ink: var(--ink); }

  .brand-top {
    position: absolute; top: 8px; right: 9px;
    color: #fff; font-size: 25px; line-height: 1;
  }
  .vitamin {
    position: absolute; left: 0; right: 0; top: 112px;
    text-align: center; color: var(--ink); font-size: 28px; line-height: 1;
  }
  .tagline {
    position: absolute; left: 70px; width: 150px; top: 181px;
    text-align: center; color: #fff;
    font-family: "Jost", "Futura", sans-serif; font-size: 8.5px; letter-spacing: 1px; line-height: 12px;
  }
  .pitch {
    position: absolute; top: 14px; right: 12px; text-align: right;
    color: var(--back-ink); font-size: 13px; line-height: 17px;
  }
  .brand-bottom {
    position: absolute; left: 9px; bottom: 14px;
    color: #fff; font-size: 25px; line-height: 1;
  }

  .photo { fill: url(#photoTone); }
  .band { fill: url(#bandTone); }
  .frame-white { fill: none; stroke: #f2f2f2; stroke-width: 3; }
  .frame-accent { fill: none; stroke: var(--accent); stroke-width: 3; }
  .ribbon { fill: var(--ribbon); }
</style>
</head>
<body>
<svg width="0" height="0" style="position:absolute" aria-hidden="true">
  <defs>
    <linearGradient id="bandTone" x1="0" y1="0" x2="1" y2="1">
      <stop offset="0" stop-color="#d2d2d2"/>
      <stop offset="0.5" stop-color="#ececec"/>
      <stop offset="1" stop-color="#a8a8a8"/>
    </linearGradient>
    <linearGradient id="photoTone" x1="0" y1="0" x2="0" y2="1">
      <stop offset="0" stop-color="#8e8676"/>
      <stop offset="0.45" stop-color="#5e5a55"/>
      <stop offset="1" stop-color="#3a3a3c"/>
    </linearGradient>
  </defs>
</svg>

<main class="sheet">

  <!-- Community -->
  <section class="card front theme-orange" style="left:50px;top:125px">
    <svg class="art" viewBox="0 0 250 250" aria-hidden="true">
      <polygon class="band" points="0,10 70,22 180,60 250,120 250,250 225,250 120,218 0,192"/>
      <rect class="frame-white" x="32" y="48" width="200" height="132" transform="rotate(2 132 114)"/>
      <rect class="frame-accent" x="26" y="63" width="196" height="131"/>
      <path class="ribbon" d="M70 181 H205 Q212 172 208 160 Q222 168 214 188 Q210 194 200 194 H70 Z"/>
    </svg>
    <p class="brand-top">paper lantern?</p>
    <h2 class="vitamin">Vitamin Community</h2>
    <p class="tagline">You belong here.</p>
  </section>
  <section class="card back theme-orange" style="left:306px;top:125px">
    <svg class="art" viewBox="0 0 250 250">
      <polygon class="photo" role="img" aria-label="Photo: two people wrapped in a flag looking down a winding road" points="0,18 90,30 200,70 250,120 250,250 215,250 120,225 0,215"/>
      <rect class="frame-white" x="32" y="48" width="200" height="132" transform="rotate(2 132 114)"/>
      <rect class="frame-accent" x="26" y="63" width="196" height="131"/>
    </svg>
    <p class="pitch">Support our movement and help us build Boston's<br>first AR map www.paper-lantern.org</p>
    <p class="brand-bottom">paper lantern?</p>
  </section>

  <!-- Agency -->
  <section class="card front theme-green" style="left:631px;top:125px">
    <svg class="art" viewBox="0 0 250 250" aria-hidden="true">
      <polygon class="band" points="0,10 70,22 180,60 250,120 250,250 225,250 120,218 0,192"/>
      <rect class="frame-white" x="32" y="48" width="200" height="132" transform="rotate(2 132 114)"/>
      <rect class="frame-accent" x="26" y="63" width="196" height="131"/>
      <path class="ribbon" d="M70 181 H205 Q212 172 208 160 Q222 168 214 188 Q210 194 200 194 H70 Z"/>
    </svg>
    <p class="brand-top">paper lantern?</p>
    <h2 class="vitamin">Vitamin Agency</h2>
    <p class="tagline">You have power.</p>
  </section>
  <section class="card back theme-green" style="left:886px;top:125px">
    <svg class="art" viewBox="0 0 250 250">
      <polygon class="photo" role="img" aria-label="Photo: two people wrapped in a flag looking down a winding road" points="0,18 90,30 200,70 250,120 250,250 215,250 120,225 0,215"/>
      <rect class="frame-white" x="32" y="48" width="200" height="132" transform="rotate(2 132 114)"/>
      <rect class="frame-accent" x="26" y="63" width="196" height="131"/>
    </svg>
    <p class="pitch">Support our movement and help us build Boston's<br>first AR map www.paper-lantern.org</p>
    <p class="brand-bottom">paper lantern?</p>
  </section>

  <!-- Empathy -->
  <section class="card front theme-red" style="left:50px;top:454px">
    <svg class="art" viewBox="0 0 250 250" aria-hidden="true">
      <polygon class="band" points="0,10 70,22 180,60 250,120 250,250 225,250 120,218 0,192"/>
      <rect class="frame-white" x="32" y="48" width="200" height="132" transform="rotate(2 132 114)"/>
      <rect class="frame-accent" x="26" y="63" width="196" height="131"/>
      <path class="ribbon" d="M70 181 H205 Q212 172 208 160 Q222 168 214 188 Q210 194 200 194 H70 Z"/>
    </svg>
    <p class="brand-top">paper lantern?</p>
    <h2 class="vitamin">Vitamin Empathy</h2>
    <p class="tagline">We all matter.</p>
  </section>
  <section class="card back theme-red" style="left:306px;top:454px">
    <svg class="art" viewBox="0 0 250 250">
      <polygon class="photo" role="img" aria-label="Photo: two people wrapped in a flag looking down a winding road" points="0,18 90,30 200,70 250,120 250,250 215,250 120,225 0,215"/>
      <rect class="frame-white" x="32" y="48" width="200" height="132" transform="rotate(2 132 114)"/>
      <rect class="frame-accent" x="26" y="63" width="196" height="131"/>
    </svg>
    <p class="pitch">Support our movement and help us build Boston's<br>first AR map www.paper-lantern.org</p>
    <p class="brand-bottom">paper lantern?</p>
  </section>

  <!-- Context -->
  <section class="card front theme-purple" style="left:631px;top:454px">
    <svg class="art" viewBox="0 0 250 250" aria-hidden="true">
      <polygon class="band" points="0,10 70,22 180,60 250,120 250,250 225,250 120,218 0,192"/>
      <rect class="frame-white" x="32" y="48" width="200" height="132" transform="rotate(2 132 114)"/>
      <rect class="frame-accent" x="26" y="63" width="196" height="131"/>
      <path class="ribbon" d="M50 181 H205 Q212 172 208 160 Q222 168 214 188 Q210 194 200 194 H50 Z"/>
    </svg>
    <p class="brand-top">paper lantern?</p>
    <h2 class="vitamin">Vitamin Context</h2>
    <p class="tagline" style="left:50px;width:170px">You understand the full picture.</p>
  </section>
  <section class="card back theme-purple" style="left:886px;top:454px">
    <svg class="art" viewBox="0 0 250 250">
      <polygon class="photo" role="img" aria-label="Photo: two people wrapped in a flag looking down a winding road" points="0,18 90,30 200,70 250,120 250,250 215,250 120,225 0,215"/>
      <rect class="frame-white" x="32" y="48" width="200" height="132" transform="rotate(2 132 114)"/>
      <rect class="frame-accent" x="26" y="63" width="196" height="131"/>
    </svg>
    <p class="pitch">Support our movement and help us build Boston's<br>first AR map www.paper-lantern.org</p>
    <p class="brand-bottom">paper lantern?</p>
  </section>

  <!-- Imagination -->
  <section class="card front theme-yellow" style="left:58px;top:766px">
    <svg class="art" viewBox="0 0 250 250" aria-hidden="true">
      <polygon class="band" points="0,10 70,22 180,60 250,120 250,250 225,250 120,218 0,192"/>
      <rect class="frame-white" x="32" y="48" width="200" height="132" transform="rotate(2 132 114)"/>
      <rect class="frame-accent" x="26" y="63" width="196" height="131"/>
      <path class="ribbon" d="M70 181 H205 Q212 172 208 160 Q222 168 214 188 Q210 194 200 194 H70 Z"/>
    </svg>
    <p class="brand-top">paper lantern?</p>
    <h2 class="vitamin">Vitamin Imagination</h2>
    <p class="tagline">Dare to dream.</p>
  </section>
  <section class="card back theme-yellow" style="left:322px;top:766px">
    <svg class="art" viewBox="0 0 250 250">
      <polygon class="photo" role="img" aria-label="Photo: two people wrapped in a flag looking down a winding road" points="0,18 90,30 200,70 250,120 250,250 215,250 120,225 0,215"/>
      <rect class="frame-white" x="32" y="48" width="200" height="132" transform="rotate(2 132 114)"/>
      <rect class="frame-accent" x="26" y="63" width="196" height="131"/>
    </svg>
    <p class="pitch">Support our movement and help us build Boston's<br>first AR map www.paper-lantern.org</p>
    <p class="brand-bottom">paper lantern?</p>
  </section>

</main>
</body>
</html>
```